Logo for Real Estate Company
Stationary and Business Cards
Simple
Glen Moravek
Broker
412 N. Calloway
Whitney, TX
moravekhomes@briskmail.example
www.moravekproperties.example

```html
<!DOCTYPE html>
<html lang="en">
<head>
<meta charset="utf-8">
<title>Moravek &amp; Associates Real Estate — Business Card</title>
<link href="https://fonts.googleapis.com/css2?family=Roboto:wght@400;500;700&display=swap" rel="stylesheet">
<style>
  :root{
    --bg:#e4e5e7;
    --blue:#2a8ad6;
    --blue-deep:#1a6cbd;
    --green:#7cc242;
    --ink:#4a4f55;
    --rule:#c8ccd0;
    --white:#ffffff;
  }
  *{box-sizing:border-box;margin:0;padding:0}
  html,body{width:1200px;height:984px;overflow:hidden;background:var(--bg);font-family:"Roboto",Arial,sans-serif}
  .stage{position:relative;width:1200px;height:984px}
  .card{position:absolute;left:220px;width:760px;height:434px;border-radius:26px;overflow:hidden;box-shadow:0 10px 28px rgba(0,0,0,.18)}
  .card--front{top:38px;background:linear-gradient(135deg,var(--blue) 0%,var(--blue-deep) 100%)}
  .card--back{top:512px;background:var(--white)}

  .front-mark{position:absolute;left:70px;top:70px;width:300px;height:220px;border-radius:12px;background:linear-gradient(160deg,rgba(255,255,255,.35),rgba(255,255,255,.12))}
  .front-name{position:absolute;right:56px;top:250px;color:var(--white);font-weight:700;line-height:1}
  .front-name .line1{display:block;font-size:30px}
  .front-name .line2{display:block;font-size:52px;margin-top:6px}

  .back-wave{position:absolute;left:0;bottom:0;width:760px;height:170px}
  .back-logo{position:absolute;left:300px;top:58px;display:flex;align-items:center;gap:10px;color:var(--green);font-weight:700;line-height:1}
  .back-logo .dot{width:22px;height:22px;border-radius:50%;background:var(--green)}
  .back-logo .l1{display:block;font-size:19px}
  .back-logo .l2{display:block;font-size:34px;margin-top:3px}

  .person{position:absolute;right:400px;top:150px;text-align:right}
  .person__name{color:var(--blue);font-size:19px;font-weight:700}
  .person__role{color:var(--ink);font-size:14px;margin-top:2px}
  .person__addr{color:var(--ink);font-size:14px;margin-top:16px;line-height:1.45}
  .divider{position:absolute;left:372px;top:150px;width:1px;height:120px;background:var(--rule)}

  .contacts{position:absolute;left:390px;top:150px;list-style:none}
  .contacts li{display:flex;align-items:center;gap:8px;color:var(--ink);font-size:14px;height:23px}
  .contacts svg{width:15px;height:15px;flex:none}
</style>
</head>
<body>
<main class="stage">

  <section class="card card--front" aria-label="Card front">
    <div class="front-mark" role="img" aria-label="Area for the company emblem"></div>
    <div class="front-name">
      <span class="line1">Moravek &amp; Associates</span>
      <span class="line2">Real Estate</span>
    </div>
  </section>

  <section class="card card--back" aria-label="Card back">
    <div class="back-logo">
      <span class="dot"></span>
      <span class="text"><span class="l1">Moravek &amp; Associates</span><span class="l2">Real Estate</span></span>
    </div>

    <div class="person">
      <p class="person__name">Glen Moravek</p>
      <p class="person__role">Broker</p>
      <p class="person__addr">412 N. Calloway<br>Alder Ridge, ST 00000</p>
    </div>
    <div class="divider"></div>

    <ul class="contacts">
      <li><svg viewBox="0 0 16 16"><circle cx="8" cy="8" r="8" fill="#2a8ad6"/><path d="M5 4.5l1.6-.4.9 2-1 .8a5 5 0 0 0 2.6 2.6l.8-1 2 .9-.4 1.6C8 11.5 4.5 8 5 4.5z" fill="#fff"/></svg>555-014-2201</li>
      <li><svg viewBox="0 0 16 16"><circle cx="8" cy="8" r="8" fill="#2a8ad6"/><rect x="5.5" y="3.5" width="5" height="9" rx="1" fill="#fff"/></svg>555-014-3307</li>
      <li><svg viewBox="0 0 16 16"><circle cx="8" cy="8" r="8" fill="#2a8ad6"/><rect x="4" y="6" width="8" height="5" fill="#fff"/><rect x="5.5" y="4" width="5" height="2" fill="#fff"/></svg>555-014-0096</li>
      <li><svg viewBox="0 0 16 16"><circle cx="8" cy="8" r="8" fill="#2a8ad6"/><rect x="4" y="5" width="8" height="6" fill="#fff"/><path d="M4 5l4 3.5L12 5" stroke="#2a8ad6" fill="none"/></svg>moravekhomes@briskmail.example</li>
      <li><svg viewBox="0 0 16 16"><circle cx="8" cy="8" r="8" fill="#2a8ad6"/><circle cx="8" cy="8" r="4" fill="none" stroke="#fff" stroke-width="1.2"/><path d="M4 8h8M8 4v8" stroke="#fff" stroke-width="1"/></svg>www.moravekproperties.example</li>
    </ul>

    <svg class="back-wave" viewBox="0 0 760 170" preserveAspectRatio="none" aria-hidden="true">
      <path d="M0 70 C180 150 420 150 760 20 L760 170 L0 170 Z" fill="#2a8ad6"/>
      <path d="M0 52 C180 132 420 132 760 2" fill="none" stroke="#7cc242" stroke-width="8"/>
    </svg>
  </section>

</main>
</body>
</html>
```